Business Card Stationary for new Logo Skin Care Studio
BusinessCard, LetterHead, Envelope. EmailSignature, Tri-fold (background only)
Professional
Marisol Quenby
41726 Calle Ondulada #219
Alderwood Hills, CA 92688
marisolquenby@postvelna.com
www.skinbymarisol.com
BusinessCard, LetterHead, Envelope. EmailSignature,
one page background (matching other stationary) that can be used for brochure
Thanks
no email address on business card!
two lines for :
next appointment;

```html
<!DOCTYPE html>
<html lang="en">
<head>
<meta charset="utf-8">
<title>Marisol's Coastal Skin Studio – Business Card Options</title>
<link href="https://fonts.googleapis.com/css2?family=Nunito:ital,wght@0,400;0,600;0,800;1,600&display=swap" rel="stylesheet">
<style>
  :root{
    --board:#3c3c3c;
    --board-dark:#2a2a2a;
    --card-white:#ffffff;
    --card-dark:#0e1a0c;
    --green:#5aa51c;
    --green-light:#9ccc2c;
    --lime:#c4e04a;
    --ink:#444;
    --label:#e6e6e6;
    --rule:#7bb33a;
  }
  *{box-sizing:border-box;margin:0;padding:0}
  html,body{width:1200px;height:809px;overflow:hidden}
  body{
    background:radial-gradient(ellipse at center,var(--board) 0%,var(--board-dark) 100%);
    font-family:'Nunito',sans-serif;position:relative;
  }
  .card{
    position:absolute;width:504px;height:293px;border-radius:16px;overflow:hidden;
    box-shadow:0 3px 10px rgba(0,0,0,.55);
  }
  .card svg.bg{position:absolute;inset:0;width:100%;height:100%}
  .front-a{left:72px;top:36px;background:var(--card-white)}
  .front-b{left:636px;top:36px;background:var(--card-dark)}
  .back-a{left:72px;top:425px;background:var(--card-white)}
  .back-b{left:636px;top:425px;background:var(--card-white)}
  .label{
    position:absolute;width:504px;text-align:center;color:var(--label);
    font-size:18px;letter-spacing:2px;font-variant:small-caps;font-weight:600;
  }
  .label-a{left:72px}.label-b{left:636px}
  .label-top{top:346px}.label-bottom{top:722px}

  .brand{position:absolute;left:0;width:100%;text-align:center;top:32px}
  .brand-mark{width:54px;height:54px;border-radius:50%;background:var(--green-light);margin:0 auto 2px}
  .brand-name{font-size:42px;font-weight:800;color:var(--green);line-height:1.05}
  .brand-sub{font-size:11px;font-weight:800;color:var(--green);letter-spacing:3px;margin-top:2px;text-transform:uppercase}
  .front-b .brand-mark{background:var(--green)}
  .front-b .brand-name,.front-b .brand-sub{color:var(--green-light)}
  .person{position:absolute;top:192px;width:100%;text-align:center;font-style:italic;font-weight:600;font-size:16px;color:var(--green)}
  .front-b .person{color:var(--lime)}
  .contact{position:absolute;top:243px;width:100%;text-align:center;font-size:9.5px;color:var(--ink);line-height:15px}
  .front-b .contact{color:#d8d8d8}
  .contact .ico{display:inline-block;width:8px;height:8px;border-radius:50%;background:var(--green);vertical-align:-1px;margin:0 3px 0 6px}

  .appt{position:absolute;left:20px;right:20px;font-size:10px;color:var(--ink)}
  .appt h3{font-size:11px;font-weight:800;color:var(--green);margin-bottom:14px}
  .field{display:flex;align-items:flex-end;margin-bottom:16px;color:#666}
  .field .line{border-bottom:1px solid var(--rule);height:1px;margin-left:6px}
  .days{display:flex;gap:14px;margin:4px 0 30px}
  .day{display:flex;align-items:center;gap:4px;color:#666;font-size:8.5px}
  .box{width:12px;height:12px;border:1px solid var(--rule)}
  .policy h4{font-size:9px;font-weight:800;color:var(--green);margin-bottom:2px}
  .policy p{font-size:8.5px;color:var(--green)}
</style>
</head>
<body>

<section class="card front-a">
  <svg class="bg" viewBox="0 0 504 293" preserveAspectRatio="none" aria-hidden="true">
    <defs>
      <linearGradient id="wave-a" x1="0" y1="0" x2="1" y2="0">
        <stop offset="0" stop-color="#c4e04a"/><stop offset="1" stop-color="#3e8e12"/>
      </linearGradient>
    </defs>
    <path d="M0 0H504V80C390 112 280 48 160 50C85 52 30 70 0 82Z" fill="url(#wave-a)"/>
    <path d="M0 82C40 66 100 56 170 58C280 62 390 122 504 80V92C390 134 280 74 170 70C100 68 40 78 0 94Z" fill="#e5f2c6"/>
  </svg>
  <div class="brand">
    <div class="brand-mark"></div>
    <div class="brand-name">Marisol's</div>
    <div class="brand-sub">Coastal Skin Studio</div>
  </div>
  <div class="person">Marisol Quenby</div>
  <div class="contact">
    <span class="ico"></span>949-555-0147<span class="ico"></span>949-555-0182<span class="ico"></span>www.skinbymarisol.com<br>
    41726 Calle Ondulada #219 Alderwood Hills, CA 92688
  </div>
</section>
<div class="label label-a label-top">Business Card Front Option A</div>

<section class="card front-b">
  <svg class="bg" viewBox="0 0 504 293" preserveAspectRatio="none" aria-hidden="true">
    <defs>
      <linearGradient id="wave-b" x1="0" y1="0" x2="1" y2="0">
        <stop offset="0" stop-color="#c4e04a"/><stop offset="1" stop-color="#3e8e12"/>
      </linearGradient>
    </defs>
    <path d="M0 0H504V80C390 112 280 48 160 50C85 52 30 70 0 82Z" fill="url(#wave-b)"/>
    <path d="M0 82C40 66 100 56 170 58C280 62 390 122 504 80V96C390 136 280 78 170 74C100 72 40 80 0 96Z" fill="#0a1408"/>
  </svg>
  <div class="brand">
    <div class="brand-mark"></div>
    <div class="brand-name">Marisol's</div>
    <div class="brand-sub">Coastal Skin Studio</div>
  </div>
  <div class="person">Marisol Quenby</div>
  <div class="contact">
    <span class="ico"></span>949-555-0147<span class="ico"></span>949-555-0182<span class="ico"></span>www.skinbymarisol.com<br>
    41726 Calle Ondulada #219 Alderwood Hills, CA 92688
  </div>
</section>
<div class="label label-b label-top">Business Card Front Option B</div>

<section class="card back-a">
  <div class="appt" style="top:70px">
    <h3>Appointment</h3>
    <div class="field">Name:<span class="line" style="width:330px"></span></div>
    <div class="field">Date:<span class="line" style="width:150px"></span>&nbsp;&nbsp;Time:<span class="line" style="width:110px"></span></div>
    <div class="days">
      <span class="day"><span class="box"></span>MON</span>
      <span class="day"><span class="box"></span>TUE</span>
      <span class="day"><span class="box"></span>WED</span>
      <span class="day"><span class="box"></span>THU</span>
      <span class="day"><span class="box"></span>FRI</span>
      <span class="day"><span class="box"></span>SAT</span>
    </div>
    <div class="policy">
      <h4>Cancellation Policy</h4>
      <p>We require 24 hours cancellation for appointments otherwise a charge may be incurred.</p>
    </div>
  </div>
</section>
<div class="label label-a label-bottom">Business Card Back Option A</div>

<section class="card back-b">
  <div class="appt" style="top:156px">
    <h3>Appointment</h3>
    <div class="field">Name:<span class="line" style="width:360px"></span></div>
    <div class="field">Date:<span class="line" style="width:170px"></span>&nbsp;&nbsp;Time:<span class="line" style="width:160px"></span></div>
  </div>
</section>
<div class="label label-b label-bottom">Business Card Back Option B</div>

</body>
</html>
```